Distribution company seeks to update marketing Brochure/Collateral

Want to take our existing mock-up in ppt format and convert to a more professional layout/design. This is a single sheet, two sided document to be given to prospective customers. File should be in a format ready to send to a printer. Take the text content we have provided and put it into an appealing format with whatever images are required to visually convey our message.
Target Market(s)
Manufacturing, Food Processing, Retail Chains, Banks
Industry/Entity Type
Marketing
Font styles to use
Serif
Other font styles liked:
- Use Font in submitted documents or similar
Requirements
Must have
- Graphics should be representative of a distribution company

```html
<!DOCTYPE html>
<html lang="en">
<head>
<meta charset="utf-8">
<title>Tidewater Supply – Brochure</title>
<link href="https://fonts.googleapis.com/css2?family=PT+Sans:ital,wght@0,400;0,700;1,400;1,700&display=swap" rel="stylesheet">
<style>
:root{
  --bg:#e9e7e3;
  --dark:#4b4b4e;
  --slate:#7a8ea6;
  --slate-deep:#5f7188;
  --mist:#c8c8ca;
  --paper:#ffffff;
  --brand:#6670b8;
  --ink:#2b2b2e;
  --teal:#3f8fa1;
  --tick:#7a8ea6;
}
*{box-sizing:border-box;margin:0;padding:0}
html,body{width:1200px;height:1048px;overflow:hidden}
body{background:var(--bg);font-family:"PT Sans",Arial,sans-serif;color:var(--ink);position:relative}
.sheet{position:absolute;width:505px;background:var(--paper);box-shadow:0 2px 8px rgba(0,0,0,.18);overflow:hidden}
.sheet--front{left:38px;top:52px;height:703px}
.sheet--back{left:604px;top:287px;height:705px}
.abs{position:absolute}
.italic{font-style:italic}

/* front */
.hero-photo{left:0;top:0;width:247px;height:268px;background:linear-gradient(180deg,#9a8d78 0%,#6d5e4b 45%,#b6a58a 100%)}
.hero-side{left:247px;top:0;width:258px;height:268px;background:linear-gradient(180deg,#fafafa,#d9d9db)}
.url{left:0;width:258px;top:26px;text-align:center;font-size:19px;font-style:italic;color:#333}
.brand-name{left:0;width:258px;top:111px;text-align:center;font-size:19px;font-weight:700;color:var(--brand);letter-spacing:.3px}
.brand-mark{left:73px;top:64px;width:14px;height:14px;background:var(--brand)}
.brand-tag{left:0;width:258px;top:134px;text-align:center;font-size:12.5px;color:var(--brand)}
.dots{left:22px;width:212px;top:162px;border-top:2px dotted #777}
.hero-quote{left:21px;top:178px;font-size:17px;font-style:italic;line-height:24px;color:#222}
.intro-band{left:0;top:268px;width:505px;height:80px;background:var(--dark);color:#fff;font-size:11.5px;line-height:14.6px;padding:10px 14px 0 16px}
.issues{left:0;top:348px;width:160px;height:300px;background:var(--slate);color:#fff;padding:14px 6px 0 9px}
.issues h3{font-size:11.5px;font-style:italic;font-weight:400;line-height:14px;margin-bottom:16px}
.issues li{list-style:none;font-size:11px;font-style:italic;line-height:13px;margin-bottom:3.6px;padding-left:6px;text-indent:-6px}
.challenges{left:160px;top:348px;width:345px;height:138px;background:var(--paper)}
.challenges h2{position:absolute;left:14px;top:10px;font-size:17px;font-style:italic;font-weight:400}
.check{position:absolute;display:flex;gap:6px;font-size:9.5px;font-style:italic;line-height:10.8px}
.check svg{flex:none;width:18px;height:18px}
.help{left:160px;top:486px;width:345px;height:162px;background:var(--mist)}
.help h2{position:absolute;left:0;width:345px;top:6px;text-align:center;font-size:17px;font-style:italic;font-weight:400}
.service{position:absolute;width:106px;height:60px;background:var(--slate);border:1px solid var(--dark)}
.service .head{background:var(--dark);color:#fff;font-size:9px;font-style:italic;text-align:center;line-height:11.5px;height:27px;display:flex;align-items:center;justify-content:center}
.service .body{color:#fff;font-size:6.2px;font-style:italic;text-align:center;line-height:7.6px;padding:4px 3px 0}
.footer{left:0;bottom:0;width:505px;height:55px;background:var(--dark);color:#fff;font-size:9px;line-height:11px;padding:12px 0 0 12px}
.foot-brand{position:absolute;right:20px;top:20px;text-align:center;color:#fff}
.foot-brand b{display:block;font-size:7px;font-weight:700;letter-spacing:.2px}
.foot-brand span{display:block;font-size:4.5px}

/* back */
.web-list{left:0;top:0;width:161px;height:651px;background:var(--slate);color:#fff;padding:30px 6px 0 9px}
.web-list h3{font-size:13.5px;font-style:italic;font-weight:400;line-height:17px;margin-bottom:10px}
.web-list li{list-style:none;font-size:11px;font-style:italic;line-height:13.6px;margin-bottom:9.3px}
.web-list h3.second{margin-top:40px;margin-bottom:14px}
.web-list ul.tight li{font-size:10.5px;line-height:13px;margin-bottom:10.5px}
.web-list .sep{border-top:2px dotted #e6e9ee;width:146px;margin-bottom:12px}
.web-head{left:161px;top:0;width:344px;height:51px;background:var(--dark);color:#fff;font-size:17px;font-style:italic;text-align:center;line-height:57px}
.web-panel{left:161px;top:51px;width:344px;height:214px;background:var(--mist)}
.screens{left:12px;top:34px;width:150px;height:120px;background:linear-gradient(180deg,#ffffff,#dfe5ee);box-shadow:3px 4px 8px rgba(0,0,0,.3)}
.feature{position:absolute;left:168px;display:flex;gap:5px;font-size:9.3px;font-style:italic;line-height:10.8px}
.feature svg{flex:none;width:16px;height:14px}
.brand-block{left:161px;top:265px;width:344px;height:168px;background:var(--paper);text-align:center}
.brand-block .sq{position:absolute;left:164px;top:38px;width:16px;height:16px;background:#1f1f1f}
.brand-block b{position:absolute;left:0;width:344px;top:60px;font-size:18px;letter-spacing:.3px;color:#1f1f1f}
.brand-block span{position:absolute;left:0;width:344px;top:83px;font-size:12.5px;color:#1f1f1f}
.print-band{left:161px;top:433px;width:344px;height:53px;background:var(--dark);color:#fff;font-size:17px;font-style:italic;text-align:center;line-height:18.5px;padding-top:9px}
.print-panel{left:161px;top:486px;width:344px;height:165px;background:var(--mist)}
.label-photo{left:26px;top:22px;width:112px;height:112px;border-radius:50%;background:radial-gradient(circle at 40% 40%,#e3cf9d,#b56a3e 55%,#6d8e8c)}
.print-spec{right:29px;top:17px;text-align:right;font-size:13.5px;font-style:italic;line-height:18.6px}
.sqf-pill{left:94px;top:93px;width:218px;height:57px;background:var(--teal);border-radius:12px;color:#fff;font-size:12px;font-style:italic;line-height:13.5px;padding:17px 0 0 48px}
</style>
</head>
<body>

<section class="sheet sheet--front">
  <div class="abs hero-photo" role="img" aria-label="Photo of a warehouse aisle with tall shelves stacked with boxed inventory"></div>
  <div class="abs hero-side">
    <div class="abs url">www.tidewatersupply.example</div>
    <div class="abs brand-mark"></div>
    <div class="abs brand-name">TIDEWATER SUPPLY</div>
    <div class="abs brand-tag">Packaging • Printing • Distribution</div>
    <div class="abs dots"></div>
    <p class="abs hero-quote">Time spent on procurement<br>is time that could be better<br>spent growing your business.</p>
  </div>

  <p class="abs intro-band">Tidewater Supply is your Single Source Solution partner for everything you need to operate your business. From general supplies to packaging and retail support including full-service flexographic printing, Tidewater can meet your demands while reducing costs and improving efficiency every day.</p>

  <div class="abs issues">
    <h3>Have you experienced any of these issues with your current supplier?</h3>
    <ul>
      <li>• Frequent backorders or lack of sufficient inventory</li>
      <li>• Billing Errors</li>
      <li>• Long Lead Times</li>
      <li>• High Minimum order amounts</li>
      <li>• Inability to source correct products</li>
      <li>• Simply taking your orders without adding value or offering better solutions</li>
      <li>• Difficulty in ordering process</li>
      <li>• Poor Customer Service</li>
      <li>• Inability to deliver product when and where needed.</li>
      <li>• Inflexibility</li>
    </ul>
  </div>

  <div class="abs challenges">
    <h2>We understand your procurement challenges.</h2>
    <div class="check" style="left:10px;top:42px"><svg viewBox="0 0 18 18"><rect x="1" y="2" width="15" height="15" fill="#fff" stroke="#7a8ea6" stroke-width="1.6"/><path d="M4 9l4 4 9-11" fill="none" stroke="#7a8ea6" stroke-width="2.6"/></svg><span>Are you managing purchases<br>with multiple vendors across<br>multiple locations, departments<br>or business units?</span></div>
    <div class="check" style="left:182px;top:42px"><svg viewBox="0 0 18 18"><rect x="1" y="2" width="15" height="15" fill="#fff" stroke="#7a8ea6" stroke-width="1.6"/><path d="M4 9l4 4 9-11" fill="none" stroke="#7a8ea6" stroke-width="2.6"/></svg><span>Would you like to lower your<br>indirect supply spend across<br>multiple categories<br>and suppliers?</span></div>
    <div class="check" style="left:10px;top:94px"><svg viewBox="0 0 18 18"><rect x="1" y="2" width="15" height="15" fill="#fff" stroke="#7a8ea6" stroke-width="1.6"/><path d="M4 9l4 4 9-11" fill="none" stroke="#7a8ea6" stroke-width="2.6"/></svg><span>Would you like to consolidate<br>your indirect supply purchases<br>on one time-saving order platform?</span></div>
    <div class="check" style="left:182px;top:94px"><svg viewBox="0 0 18 18"><rect x="1" y="2" width="15" height="15" fill="#fff" stroke="#7a8ea6" stroke-width="1.6"/><path d="M4 9l4 4 9-11" fill="none" stroke="#7a8ea6" stroke-width="2.6"/></svg><span>Would you like to prevent<br>spending abuse?</span></div>
  </div>

  <div class="abs help">
    <h2>How can Tidewater help?</h2>
    <div class="service" style="left:6px;top:32px"><div class="head">Sourcing and<br>Procurement Support</div><div class="body">Let us manage your suppliers while you manage your business, saving money and time</div></div>
    <div class="service" style="left:119px;top:32px"><div class="head">Warehousing and<br>Fulfillment</div><div class="body">Our distribution centers allow us to efficiently manage fulfillment and delivery of supplies</div></div>
    <div class="service" style="left:232px;top:32px"><div class="head">Inventory<br>Management</div><div class="body">We allow our customers to remain competitive while avoiding overstocks and shortages</div></div>
    <div class="service" style="left:6px;top:97px"><div class="head">Specialty Printing</div><div class="body">SQF certified manufacturer of plain and printed labels up to 8-colors</div></div>
    <div class="service" style="left:119px;top:97px"><div class="head">Integrated IT<br>Order Management</div><div class="body">Customer-specific reporting and web ordering allow you to conduct business at your convenience</div></div>
    <div class="service" style="left:232px;top:97px"><div class="head">Packaging</div><div class="body">From common corrugated to specialized, custom product packaging</div></div>
  </div>

  <footer class="abs footer">
    1420 Harborline Drive,<br>Suite 6 Riverton, FL 32000<br>Phone (555) 014 - 2288
    <div class="foot-brand"><b>TIDEWATER SUPPLY</b><span>Packaging • Printing • Distribution</span></div>
  </footer>
</section>

<section class="sheet sheet--back">
  <div class="abs web-list">
    <h3>What can our Web platform do for you?</h3>
    <ul>
      <li>• Make purchasing easier</li>
      <li>• Control your spend and improve cash flow</li>
      <li>• Prevent spending abuse</li>
      <li>• Identify trends and patterns</li>
      <li>• Gain purchasing efficiencies with real-time order tracking</li>
      <li>• Manage multiple business units or locations with ease</li>
    </ul>
    <h3 class="second">Better supply chain performance and value with Tidewater Supply</h3>
    <ul class="tight">
      <li>• Cost Reduction on Direct and Indirect spend</li>
      <li>• Strategic Sourcing - access to our network of suppliers for specialty items unique to your industry</li>
      <li>• Seamless ordering of large quantity Items without inventory holding costs, reducing working capital and preventing overstocking and supply shortage</li>
      <li>• Better Management, Control, and purchasing analysis</li>
      <li>• Ease of ordering through proprietary online ordering system (Web View), FTP, file transfer and EDI</li>
    </ul>
  </div>

  <div class="abs web-head">Web Platform Design</div>
  <div class="abs web-panel">
    <div class="abs screens" role="img" aria-label="Stacked screenshots of the online ordering storefront and order tables"></div>
    <div class="feature" style="top:18px"><svg viewBox="0 0 16 14"><path d="M1 7l5 5 9-11" fill="none" stroke="#7a8ea6" stroke-width="3"/></svg><span>User-friendly storefront<br>Web interface</span></div>
    <div class="feature" style="top:44px"><svg viewBox="0 0 16 14"><path d="M1 7l5 5 9-11" fill="none" stroke="#7a8ea6" stroke-width="3"/></svg><span>Each user has their own<br>User ID and password</span></div>
    <div class="feature" style="top:73px"><svg viewBox="0 0 16 14"><path d="M1 7l5 5 9-11" fill="none" stroke="#7a8ea6" stroke-width="3"/></svg><span>Purchases are mapped to<br>the particular User/ Department</span></div>
    <div class="feature" style="top:101px"><svg viewBox="0 0 16 14"><path d="M1 7l5 5 9-11" fill="none" stroke="#7a8ea6" stroke-width="3"/></svg><span>Dashboard allows User to<br>quickly review most current<br>order and previous orders</span></div>
    <div class="feature" style="top:140px"><svg viewBox="0 0 16 14"><path d="M1 7l5 5 9-11" fill="none" stroke="#7a8ea6" stroke-width="3"/></svg><span>Communicate messages to<br>users via the website</span></div>
    <div class="feature" style="top:169px"><svg viewBox="0 0 16 14"><path d="M1 7l5 5 9-11" fill="none" stroke="#7a8ea6" stroke-width="3"/></svg><span>Chat with TWS Customer<br>Support regarding your orders</span></div>
  </div>

  <div class="abs brand-block">
    <div class="sq"></div>
    <b>TIDEWATER SUPPLY</b>
    <span>Packaging • Printing • Distribution</span>
  </div>

  <div class="abs print-band">Consolidate: We Also Offer Full Service<br>In-house Flexographic Printing</div>
  <div class="abs print-panel">
    <div class="abs sqf-pill">Fully Integrated, SQF Certified<br>Flexographic Printing</div>
    <div class="abs label-photo" role="img" aria-label="Assorted printed product labels and tags fanned out"></div>
    <p class="abs print-spec">Up to 8 colors<br>Paper, Synthetic Label, Tags,<br>BOPP, +Others</p>
  </div>

  <footer class="abs footer">
    1420 Harborline Drive,<br>Suite 6 Riverton, FL 32000<br>Phone (555) 014 - 2288
    <div class="foot-brand"><b>TIDEWATER SUPPLY</b><span>Packaging • Printing • Distribution</span></div>
  </footer>
</section>

</body>
</html>
```